TWR Business Card Design

As a full service media and advocacy firm, we lean on years of experience in political and corporate consulting, grassroots campaigning, media placement, and video production to deliver unparalleled results. Recently we have moved into digital media and now provide this service for our clients.

I will add our two company logos to be used on the business cards. The longer logo with "sky reach studio" is our primary logo. Our secondary logo is more square one with "sky reach" and 'digital.media.campaigns" on it. We are looking for clean and modern looking business cards fitting for a digital firm.

I will also add our logos that go well with dark backgrounds.

Industry/Entity Type

Political

Contact Information for Business Card

Walter Pennick, Director of Campaigns and Digital, 555-218-4760, walter@skyreachstudioco.example, @SkyReachStudioCo, @WalterPennick, Facebook.com/SkyReachStudioCo

```html
<!DOCTYPE html>
<html lang="en">
<head>
<meta charset="utf-8">
<title>Sky Reach Studio – Business Card</title>
<link rel="stylesheet" href="https://fonts.googleapis.com/css2?family=Lato:wght@400;700;900&display=swap">
<style>
  :root {
    --page-bg: #262626;
    --band-blue: #1b8de6;
    --card-blue: #1448a6;
    --card-deep: #0b2b72;
    --ink-white: #ffffff;
    --ink-soft: #d9e8fb;
    --ink-dark: #0a1f4d;
    --icon-fill: #1b8de6;
  }
  * { box-sizing: border-box; margin: 0; padding: 0; }
  html, body {
    width: 1200px; height: 997px; overflow: hidden;
    background: var(--page-bg);
    font-family: "Lato", Arial, sans-serif;
  }
  .business-card {
    position: absolute; left: 180px; top: 246px;
    width: 840px; height: 504px;
    border-radius: 28px; overflow: hidden;
    background: linear-gradient(160deg, var(--card-blue) 0%, var(--card-deep) 100%);
    box-shadow: 0 18px 40px rgba(0,0,0,.55);
  }
  .header-band {
    position: absolute; left: 0; top: 0; width: 100%; height: 78px;
    background: var(--band-blue);
    text-align: right; padding: 12px 40px 0 0;
  }
  .holder-name { color: var(--ink-white); font-weight: 900; font-size: 26px; line-height: 1.1; }
  .holder-title { color: var(--ink-dark); font-weight: 700; font-size: 14px; margin-top: 6px; }

  .accent-band {
    position: absolute; left: 0; top: 226px; width: 100%; height: 26px;
    background: var(--band-blue);
  }
  .brand-lockup {
    position: absolute; left: 0; top: 128px; width: 100%;
    display: flex; justify-content: center; align-items: center; gap: 18px;
  }
  .brand-mark { width: 40px; height: 40px; border-radius: 50%; background: var(--band-blue); flex: none; }
  .brand-name {
    color: var(--ink-white); font-weight: 700; font-size: 60px;
    line-height: 1; letter-spacing: 1px;
  }

  .contact-band {
    position: absolute; left: 0; top: 300px; width: 100%; height: 34px;
    background: var(--band-blue);
    display: flex; align-items: center; justify-content: space-between;
    padding: 0 36px;
    color: var(--ink-white); font-weight: 700; font-size: 15px;
  }
  .contact-item { display: flex; align-items: center; gap: 10px; white-space: nowrap; }
  .contact-icon { width: 24px; height: 24px; flex: none; }

  .social-row {
    position: absolute; left: 0; top: 366px; width: 100%;
    display: flex; justify-content: space-around;
  }
  .social-item {
    display: flex; flex-direction: column; align-items: center; gap: 10px;
    color: var(--ink-soft); font-size: 18px;
  }
  .social-dot {
    width: 46px; height: 46px; border-radius: 50%;
    background: var(--icon-fill);
    display: flex; align-items: center; justify-content: center;
    color: var(--ink-white); font-weight: 700; font-size: 22px; line-height: 1;
  }
</style>
</head>
<body>
  <section class="business-card">
    <header class="header-band">
      <p class="holder-name">Walter Pennick</p>
      <p class="holder-title">Director of Campaigns and Digital</p>
    </header>

    <div class="accent-band"></div>

    <div class="brand-lockup">
      <span class="brand-mark"></span>
      <h1 class="brand-name">sky reach</h1>
    </div>

    <div class="contact-band">
      <span class="contact-item">
        <svg class="contact-icon" viewBox="0 0 24 24"><circle cx="12" cy="12" r="12" fill="#ffffff"/><path d="M6 10c0-2 2-3 6-3s6 1 6 3v1h-3v-1.5h-6V11H6z M8 12h8l1 5H7z" fill="#1b8de6"/></svg>
        555-218-4760
      </span>
      <span class="contact-item">
        <svg class="contact-icon" viewBox="0 0 24 24"><circle cx="12" cy="12" r="12" fill="#ffffff"/><rect x="6" y="8" width="12" height="8" rx="1" fill="none" stroke="#1b8de6" stroke-width="1.6"/><path d="M6.5 8.5l5.5 4 5.5-4" fill="none" stroke="#1b8de6" stroke-width="1.6"/></svg>
        walter@skyreachstudioco.example
      </span>
      <span class="contact-item">
        <svg class="contact-icon" viewBox="0 0 24 24"><circle cx="12" cy="12" r="12" fill="#ffffff"/><path d="M9 15l6-6M8.5 11.5l-1.5 1.5a2.5 2.5 0 0 0 3.5 3.5l1.5-1.5M15.5 12.5l1.5-1.5a2.5 2.5 0 0 0-3.5-3.5l-1.5 1.5" stroke="#1b8de6" stroke-width="1.8" fill="none" stroke-linecap="round"/></svg>
        www.skyreachstudioco.example
      </span>
    </div>

    <div class="social-row">
      <div class="social-item"><span class="social-dot">@</span>@SkyReachStudioCo</div>
      <div class="social-item"><span class="social-dot">@</span>@WalterPennick</div>
      <div class="social-item"><span class="social-dot">@</span>SkyReachStudioCo</div>
    </div>
  </section>
</body>
</html>
```